Reggie Vosburn - Free Personalised Health Consultation - "Every body walks its own path"

This flyer will be left on tables/seats at speaking events and seminars and used to attain leads.

Top half will have "SMS me for a FREE Personalised Health Consultation" and my picture (see www.reggievosburn.example and pick most engaging photo) and underneath my contact details. It must have lines with "Notes:" halfway down so people can take notes at the seminar and lines on the back with my contact details again and "Notes: with lines.

I am having a business card also being designed by Plotnest for same and would like the flyer and business card to carry a similar feel/look for consistency.

Below is the brief for the business card being designed:
Business Card for www.reggievosburn.example site. It is a trust site and I use it for 1:1 relatable connections. It is the one I use for building intimate 1:1 trust building and Exec Coaching Services and programs for high wealth individuals and corporates. I also have a commercial programmatic site of my personal health products and services and programs for main stream one to many. www.crossgenvitality.example that can also provoke thought for the www.reggievosburn.example business card. (mind you will get a separate business card for that site, but want to provide context). It has a logo which you may want to draw from in designing the reggievosburn business card which is personal and is about building my brand. There is also a reggievosburn personal KX page and reggievosburn business KX page. I am a Certified Talent Compass 4.1 Coach with Verrick and you can get a corporate brief of me on there to give you more context https://www.verricktalenthub.example/coach/en-us/directory?search=reggie

Target Market(s)

Exec, IT, Health conscious. Corporates wanting to run Health and Wellness programs. Those wanting to go from good to great. Millennials to Middleaged.

Industry/Entity Type

Health And Wellness

Font styles to use
Sans Serif
Other font styles liked:
• Arial and Calibri ok too

Colors

Designer to choose colors to be used in the design.

Requirements
Must have
• Picture of me - use best from www.reggievosburn.example or can send one you choose.
• Contact details like my buisness card being designed by you guys in separate project.
• Name: Reggie Vosburn
• email: reggie@reggievosburn.,example
• Phone: Australia +61 455 318 026 Singapore: +65 8342 1960
Nice to have
• Open to ideas

```html
<!DOCTYPE html>
<html lang="en">
<head>
<meta charset="utf-8">
<title>Reggie Vosburn – Flyer and Business Card</title>
<link rel="stylesheet" href="https://fonts.googleapis.com/css2?family=Montserrat:wght@300;400;800;900&family=Arimo:wght@400;700&display=swap">
<style>
  :root {
    --ink: #0d0d0d;
    --charcoal: #1c1c1c;
    --graphite: #3a3a3a;
    --steel: #5a5a5a;
    --ash: #9a9a9a;
    --rule: #c4c4c4;
    --mist: #f3f3f3;
    --paper: #ffffff;
    --stage: #e6e6e6;
    --outline-fill: #181818;
  }
  * { box-sizing: border-box; margin: 0; padding: 0; }
  html, body { width: 880px; height: 1200px; overflow: hidden; }
  body {
    background: var(--stage);
    font-family: "Arimo", Arial, sans-serif;
    color: var(--paper);
    position: relative;
  }
  .sheet { position: absolute; overflow: hidden; box-shadow: 0 2px 10px rgba(0,0,0,.12); }

  /* ---------- flyer ---------- */
  .flyer { width: 400px; height: 566px; background: var(--paper); top: 40px; }
  .flyer--front { left: 30px; }
  .flyer--back { left: 450px; }

  .hero {
    position: absolute; inset: 0 0 auto 0; height: 270px;
    background: linear-gradient(125deg, var(--graphite) 0%, var(--ink) 55%, var(--charcoal) 100%);
  }
  .hero__portrait {
    position: absolute; right: 0; top: 0; width: 205px; height: 240px;
    background: radial-gradient(ellipse at 55% 45%, #d8d8d8 0%, #8a8a8a 35%, #2a2a2a 75%, transparent 100%);
  }
  .brand-name {
    font-family: "Arimo", Arial, sans-serif; font-size: 11px; letter-spacing: .06em;
    text-transform: uppercase; color: var(--paper); white-space: nowrap;
  }
  .brand-name .rule { border-bottom: 1px solid var(--paper); padding-bottom: 2px; }
  .brand-name--small { font-size: 10px; }
  .hero .brand-name { position: absolute; left: 28px; top: 62px; }

  .headline {
    position: absolute; left: 28px; top: 108px;
    font-family: "Montserrat", Arial, sans-serif; text-transform: uppercase; line-height: 1;
    font-weight: 400;
  }
  .headline__lead { display: block; font-size: 25px; font-weight: 900; }
  .headline__for { display: block; font-size: 24px; font-weight: 300; margin-top: 2px; }
  .headline__free {
    display: block; font-size: 46px; font-weight: 900; letter-spacing: .03em;
    color: var(--outline-fill);
    text-shadow:
      1.3px 0 0 var(--paper), -1.3px 0 0 var(--paper),
      0 1.3px 0 var(--paper), 0 -1.3px 0 var(--paper),
      1px 1px 0 var(--paper), -1px -1px 0 var(--paper),
      1px -1px 0 var(--paper), -1px 1px 0 var(--paper);
  }
  .headline__offer { display: block; font-size: 14px; font-weight: 400; margin-top: 4px; line-height: 1.1; letter-spacing: .02em; }

  .email-band {
    position: absolute; right: 0; top: 242px; width: 200px; height: 28px;
    background: var(--charcoal); display: flex; align-items: center; gap: 6px;
    padding-left: 30px; font-size: 9.5px; color: #dcdcdc; white-space: nowrap;
  }
  .phone-band {
    position: absolute; left: 0; right: 0; top: 270px; height: 28px;
    background: var(--steel); display: flex; align-items: center;
    padding-left: 70px; font-size: 9.5px; color: #e4e4e4; white-space: nowrap;
  }
  .icon { width: 11px; height: 11px; flex: none; }

  .note-lines { position: absolute; left: 40px; right: 40px; }
  .note-lines span {
    display: block; height: 1px;
    background: linear-gradient(90deg, var(--rule), #e2e2e2 70%, var(--rule));
  }
  .flyer--front .note-lines { top: 340px; }
  .flyer--front .note-lines span + span { margin-top: 44px; }

  .web-tag {
    position: absolute; right: 0; height: 24px; width: 170px; background: var(--ink);
    display: flex; align-items: center; justify-content: center; font-size: 10px; color: var(--paper);
    white-space: nowrap;
  }
  .flyer .web-tag { top: 478px; }
  .base-rule { position: absolute; left: 32px; right: 0; top: 522px; height: 2px; background: var(--ink); }

  .letterhead {
    position: absolute; inset: 0 0 auto 0; height: 38px; background: var(--ink);
    display: flex; align-items: center; justify-content: flex-end; gap: 26px; padding-right: 18px;
  }
  .letterhead .email { display: flex; align-items: center; gap: 5px; font-size: 8.5px; color: #cfcfcf; white-space: nowrap; }
  .letterhead-strip {
    position: absolute; left: 0; right: 0; top: 38px; height: 20px; background: var(--steel);
    font-size: 8.5px; color: #e2e2e2; display: flex; align-items: center; padding-left: 28px; white-space: nowrap;
  }
  .back-field {
    position: absolute; left: 0; right: 0; top: 58px; bottom: 0;
    background: linear-gradient(180deg, var(--mist), #fafafa);
  }
  .back-field__ghost {
    position: absolute; right: 30px; top: 70px; width: 190px; height: 330px;
    background: linear-gradient(160deg, rgba(0,0,0,.05), rgba(0,0,0,.01));
  }
  .flyer--back .note-lines { top: 100px; left: 36px; right: 36px; }
  .flyer--back .note-lines span + span { margin-top: 31px; }

  /* ---------- business card ---------- */
  .card { width: 400px; height: 230px; top: 670px; }
  .card--front { left: 30px; background: linear-gradient(120deg, var(--graphite) 0%, var(--ink) 45%, var(--charcoal) 100%); }
  .card--back { left: 450px; background: var(--paper); }

  .card--front .brand-name { position: absolute; left: 0; right: 0; top: 78px; text-align: center; font-size: 15px; }
  .card--front .web-tag { top: 110px; background: var(--steel); width: 160px; font-size: 9.5px; }
  .directory {
    position: absolute; left: 0; right: 0; top: 150px; text-align: center;
    font-family: "Arimo", Arial, sans-serif; font-weight: 700; font-size: 20px; text-transform: uppercase;
    letter-spacing: .03em; white-space: nowrap;
    color: var(--outline-fill);
    text-shadow:
      .8px 0 0 #bdbdbd, -.8px 0 0 #bdbdbd,
      0 .8px 0 #bdbdbd, 0 -.8px 0 #bdbdbd;
  }

  .card__shape { position: absolute; inset: 0; }
  .card__ghost {
    position: absolute; right: 0; top: 0; width: 200px; height: 150px;
    background: linear-gradient(200deg, rgba(0,0,0,.06), rgba(0,0,0,0));
  }
  .card--back .brand-name { position: absolute; left: 30px; top: 170px; font-size: 14px; }
  .contacts { position: absolute; left: 226px; top: 66px; font-size: 9.5px; color: var(--graphite); line-height: 1.45; white-space: nowrap; }
  .contacts__row { display: flex; gap: 6px; align-items: flex-start; }
  .contacts__row + .contacts__row { margin-top: 6px; }
  .card--back .web-tag { top: 152px; width: 165px; font-size: 10px; }
</style>
</head>
<body>

<!-- Flyer front -->
<section class="sheet flyer flyer--front">
  <div class="hero">
    <div class="hero__portrait" role="img" aria-label="Black and white portrait photo of Reggie Vosburn"></div>
    <div class="brand-name">Reggie <span class="rule">Vosburn</span></div>
    <h1 class="headline">
      <span class="headline__lead">SMS me</span>
      <span class="headline__for">for a</span>
      <span class="headline__free">Free</span>
      <span class="headline__offer">Personalised<br>Health Consultation</span>
    </h1>
  </div>
  <div class="email-band">
    <svg class="icon" viewBox="0 0 12 12"><circle cx="6" cy="6" r="5.4" fill="none" stroke="#ccc" stroke-width=".8"/><rect x="3" y="4" width="6" height="4" fill="none" stroke="#ccc" stroke-width=".7"/><path d="M3 4l3 2.2L9 4" fill="none" stroke="#ccc" stroke-width=".7"/></svg>
    reggie@reggievosburn.example
  </div>
  <div class="phone-band">Australia +61 455 318 026 &nbsp;|&nbsp; Singapore: +65 8342 1960</div>
  <div class="note-lines"><span></span><span></span><span></span></div>
  <div class="web-tag">www.reggievosburn.example</div>
  <div class="base-rule"></div>
</section>

<!-- Flyer back -->
<section class="sheet flyer flyer--back">
  <div class="back-field"><div class="back-field__ghost" role="img" aria-label="Faint photo of an office interior with plants"></div></div>
  <div class="letterhead">
    <div class="brand-name brand-name--small">Reggie <span class="rule">Vosburn</span></div>
    <div class="email">
      <svg class="icon" viewBox="0 0 12 12"><circle cx="6" cy="6" r="5.4" fill="none" stroke="#ccc" stroke-width=".8"/><rect x="3" y="4" width="6" height="4" fill="none" stroke="#ccc" stroke-width=".7"/><path d="M3 4l3 2.2L9 4" fill="none" stroke="#ccc" stroke-width=".7"/></svg>
      reggie@reggievosburn.example
    </div>
  </div>
  <div class="letterhead-strip">Australia +61 455 318 026 &nbsp;|&nbsp; Singapore: +65 8342 1960</div>
  <div class="note-lines">
    <span></span><span></span><span></span><span></span><span></span><span></span>
    <span></span><span></span><span></span><span></span><span></span><span></span>
  </div>
  <div class="web-tag">www.reggievosburn.example</div>
  <div class="base-rule"></div>
</section>

<!-- Business card front -->
<section class="sheet card card--front">
  <div class="brand-name">Reggie <span class="rule">Vosburn</span></div>
  <div class="web-tag">www.reggievosburn.example</div>
  <div class="directory">Certified Coaches Directory</div>
</section>

<!-- Business card back -->
<section class="sheet card card--back">
  <div class="card__ghost" role="img" aria-label="Faint photo of palm leaves"></div>
  <svg class="card__shape" viewBox="0 0 400 230" preserveAspectRatio="none">
    <polygon points="0,230 0,58 190,58 255,230" fill="#0d0d0d"/>
    <polygon points="150,58 170,58 240,230 218,230" fill="#9a9a9a" opacity=".55"/>
    <polygon points="172,58 190,58 255,230 236,230" fill="#5a5a5a" opacity=".7"/>
    <polygon points="300,0 400,0 400,30 340,30" fill="#0d0d0d"/>
    <polygon points="276,0 300,0 340,30 316,30" fill="#9a9a9a" opacity=".55"/>
    <polygon points="290,0 310,0 352,30 330,30" fill="#5a5a5a" opacity=".6"/>
  </svg>
  <div class="brand-name">Reggie <span class="rule">Vosburn</span></div>
  <div class="contacts">
    <div class="contacts__row">
      <svg class="icon" viewBox="0 0 12 12"><circle cx="6" cy="6" r="5.4" fill="none" stroke="#3a3a3a" stroke-width=".8"/><rect x="4.2" y="3" width="3.6" height="6" rx=".6" fill="none" stroke="#3a3a3a" stroke-width=".7"/></svg>
      <div>Australia +61 455 318 026<br>&nbsp;&nbsp;Singapore: +65 8342 1960</div>
    </div>
    <div class="contacts__row">
      <svg class="icon" viewBox="0 0 12 12"><circle cx="6" cy="6" r="5.4" fill="none" stroke="#3a3a3a" stroke-width=".8"/><rect x="3" y="4" width="6" height="4" fill="none" stroke="#3a3a3a" stroke-width=".7"/><path d="M3 4l3 2.2L9 4" fill="none" stroke="#3a3a3a" stroke-width=".7"/></svg>
      <div>reggie@reggievosburn.example</div>
    </div>
  </div>
  <div class="web-tag">www.reggievosburn.example</div>
</section>

</body>
</html>
```